Quillmark Hall Business Card

I need a business card design. We are a collaborate online training company. Our colors are gray and green. Our website is QuillmarkHall.com

I would like an area for a profile picture within the card

```html
<!DOCTYPE html>
<html lang="en">
<head>
<meta charset="utf-8">
<title>Quillmark Hall Business Card</title>
<link href="https://fonts.googleapis.com/css2?family=Open+Sans:wght@400;600;700&display=swap" rel="stylesheet">
<style>
  :root {
    --backdrop: #4a3f3a;
    --card: #1b1b1c;
    --card-edge: #2a2a2b;
    --green: #8cc63f;
    --gray: #8d8d8f;
    --white: #f2f2f2;
    --text: #dcdcdc;
  }
  * { box-sizing: border-box; margin: 0; padding: 0; }
  html, body {
    width: 1200px; height: 787px; overflow: hidden;
    background: var(--backdrop);
    font-family: "Open Sans", Arial, sans-serif;
  }
  .stage {
    position: relative; width: 1200px; height: 787px;
    display: flex; align-items: center; justify-content: center; gap: 48px;
  }
  .card {
    position: relative; width: 530px; height: 302px;
    background: var(--card);
    border: 1px solid var(--card-edge);
    border-radius: 4px;
    overflow: hidden;
  }
  /* back side */
  .card-back .brand {
    position: absolute; left: 56px; top: 70px;
    display: flex; align-items: center; gap: 16px;
  }
  .brand-dot { width: 52px; height: 52px; border-radius: 50%; }
  .card-back .brand-dot { background: var(--gray); }
  .brand-name { font-weight: 700; letter-spacing: -0.5px; }
  .card-back .brand-name { font-size: 48px; color: var(--gray); }
  .card-back .website {
    position: absolute; left: 56px; bottom: 56px;
    font-size: 15px; letter-spacing: 5px; color: var(--text);
  }
  /* front side */
  .card-front .brand {
    position: absolute; left: 28px; top: 28px;
    display: flex; align-items: center; gap: 12px;
  }
  .card-front .brand-dot { width: 40px; height: 40px; background: var(--green); }
  .card-front .brand-name { font-size: 38px; color: var(--white); }
  .person { position: absolute; left: 30px; top: 112px; }
  .person-name { font-size: 21px; font-weight: 600; color: var(--green); line-height: 1.1; }
  .person-title { font-size: 15px; font-weight: 600; color: var(--white); margin-top: 2px; }
  .address { margin-top: 12px; font-size: 13.5px; color: var(--text); line-height: 1.35; }
  .contacts { list-style: none; margin-top: 12px; }
  .contacts li {
    display: flex; align-items: center; gap: 10px;
    font-size: 13.5px; color: var(--text); line-height: 1.75;
  }
  .contacts svg { width: 14px; height: 14px; fill: var(--green); flex: none; }
  .profile-photo {
    position: absolute; right: 0; bottom: 0; width: 190px; height: 210px;
    background: radial-gradient(ellipse at 50% 35%, #b98a6e 0%, #7a5646 40%, #3e3a3a 75%, #2a2a2c 100%);
  }
</style>
</head>
<body>
  <main class="stage">
    <section class="card card-back" aria-label="Card back">
      <div class="brand">
        <span class="brand-dot"></span>
        <span class="brand-name">Quillmark Hall</span>
      </div>
      <p class="website">www.quillmarkhall.com</p>
    </section>

    <section class="card card-front" aria-label="Card front">
      <div class="brand">
        <span class="brand-dot"></span>
        <span class="brand-name">Quillmark Hall</span>
      </div>
      <div class="person">
        <h1 class="person-name">Dana Whitlock</h1>
        <p class="person-title">Founder</p>
        <p class="address">418 E Marigold Ave, Suite 7<br>Tempe, Arizona 85281</p>
        <ul class="contacts">
          <li>
            <svg viewBox="0 0 16 16" aria-hidden="true"><path d="M3.5 1.5l2.5 0 1 3.5-1.8 1.2a9 9 0 0 0 4.6 4.6L11 9l3.5 1v2.5c0 1-1 2-2 2A11 11 0 0 1 1.5 3.5c0-1 1-2 2-2z"/></svg>
            (480) 555-0172
          </li>
          <li>
            <svg viewBox="0 0 16 16" aria-hidden="true"><path d="M1 3h14v10H1z M1.8 3.8L8 8.8l6.2-5" fill="none" stroke="#8cc63f" stroke-width="1.6"/></svg>
            dana@quillmarkhall.com
          </li>
          <li>
            <svg viewBox="0 0 16 16" aria-hidden="true"><circle cx="8" cy="8" r="6.5" fill="none" stroke="#8cc63f" stroke-width="1.5"/><path d="M1.5 8h13M8 1.5c-3 3.5-3 9.5 0 13M8 1.5c3 3.5 3 9.5 0 13" fill="none" stroke="#8cc63f" stroke-width="1.2"/></svg>
            quillmarkhall.com
          </li>
        </ul>
      </div>
      <div class="profile-photo" role="img" aria-label="Profile photo of the founder"></div>
    </section>
  </main>
</body>
</html>
```